Quick 1hr job to create exciting page header & footer designs

We need some exciting and engaging header and footer designs for school yearbooks, in particular for the NZ Primary school market (children 5 to 10 years old).
The header and footer designs need to be bright and colourful, and should appeal to younger children. Header and footer graphics do not need to be the same, but should at least relate to each other thematically.
Please include the following sample text on the header: Sports Day.
Please include this sample text on the footer: Primary School Name 2014.
Note that the header/footers may be used without the text so the design should work with or without the text. Header/footer may be used over top of a coloured or graphic background. The graphic could be illustrative, photographic or patterned, the more creative the better.

Header dimensions: 198.88 mm w x 15.24 mm h
Footer dimensions: 198.88 mm w x 6.35 mm h

Please see the example pages provided, but please note we are looking for something more suitable for Primary Schools, and a lot more dynamic and interesting!

Target Market(s)

New Zealand Primary Schools

Industry/Entity Type

School

Requirements
Must have
• Must contain sample text and must be suitable for younger children
• Must be appropriate for the New Zealand market, i.e. don't use imagery that is obviously from other countries.

```html
<!DOCTYPE html>
<html lang="en">
<head>
<meta charset="utf-8">
<title>Sports Day – Header &amp; Footer Set</title>
<link href="https://fonts.googleapis.com/css2?family=Comic+Neue:wght@400;700&family=Emilys+Candy&display=swap" rel="stylesheet">
<style>
  :root {
    --paper: #ffffff;
    --label-ink: #1a1a1a;
    --rule: #555555;
    --grass: #8dc63f;
    --red: #e8373a;
    --navy: #2b3590;
    --orange: #f05a28;
    --bunting: linear-gradient(90deg, #e8373a 0%, #f7d117 14%, #8dc63f 28%, #29abe2 42%, #ec4fa5 56%, #f7941d 70%, #8dc63f 84%, #29abe2 100%);
    --flowers: linear-gradient(90deg, #a7dff0 0%, #fbe39a 30%, #fcc890 55%, #f3a6d6 80%, rgba(255,255,255,0) 100%);
    --squares: linear-gradient(90deg, rgba(255,255,255,0) 0%, #fbd9a3 22%, #a9e3e8 45%, #f29ab3 70%, #d7a0dc 100%);
  }
  * { box-sizing: border-box; margin: 0; padding: 0; }
  html, body { width: 1200px; height: 901px; overflow: hidden; background: var(--paper); }
  .canvas { position: relative; width: 1200px; height: 901px; overflow: hidden; background: var(--paper); }

  .theme-red { --accent: var(--red); }
  .theme-navy { --accent: var(--navy); }
  .theme-orange { --accent: var(--orange); }

  .set { position: absolute; left: 0; width: 1200px; height: 260px; }

  .part-label {
    position: absolute; left: 18px;
    font-family: "Comic Neue", "Comic Sans MS", sans-serif;
    font-size: 20px; font-weight: 400; color: var(--label-ink);
  }
  .part-label.header-label { top: 13px; }
  .part-label.footer-label { top: 177px; }

  .header-band { position: absolute; left: 17px; top: 50px; width: 1161px; height: 90px; }
  .bunting { position: absolute; left: 0; top: 0; width: 100%; height: 13px; background: var(--bunting); opacity: 0.9; }
  .grass-edge { position: absolute; left: 0; bottom: 0; width: 100%; height: 7px; background: var(--grass); }
  .flower-art { position: absolute; left: 0; top: 6px; width: 245px; height: 78px; background: var(--flowers); opacity: 0.85; }
  .square-art { position: absolute; right: 0; top: 8px; width: 245px; height: 76px; background: var(--squares); opacity: 0.8; }

  .title-row {
    position: absolute; left: 305px; top: 13px; width: 585px; height: 70px;
    display: flex; align-items: center; justify-content: space-between;
  }
  .header-title {
    font-family: "Emilys Candy", cursive;
    font-size: 50px; line-height: 1; color: var(--accent); white-space: nowrap;
  }
  .stars { display: block; fill: var(--accent); }

  .footer-band { position: absolute; left: 17px; top: 209px; width: 1161px; height: 40px; }
  .footer-band .bunting { height: 10px; }
  .footer-row {
    position: absolute; left: 305px; top: 13px; width: 560px; height: 24px;
    display: flex; align-items: center; justify-content: space-between;
  }
  .footer-title {
    font-family: "Emilys Candy", cursive;
    font-size: 19px; line-height: 1; color: var(--accent); white-space: nowrap;
  }

  .divider { position: absolute; left: 17px; width: 1163px; height: 0; border-top: 1.4px solid var(--rule); }
</style>
</head>
<body>
<svg width="0" height="0" style="position:absolute" aria-hidden="true">
  <defs>
    <symbol id="star" viewBox="-10 -10 20 20">
      <polygon points="0,-10 2.35,-3.24 9.51,-3.09 3.8,1.24 5.88,8.09 0,4 -5.88,8.09 -3.8,1.24 -9.51,-3.09 -2.35,-3.24"/>
    </symbol>
    <symbol id="stars-left" viewBox="0 0 110 18">
      <use href="#star" x="0" y="4" width="10" height="10"/>
      <use href="#star" x="24" y="4" width="10" height="10"/>
      <use href="#star" x="48" y="4" width="10" height="10"/>
      <use href="#star" x="72" y="4" width="10" height="10"/>
      <use href="#star" x="93" y="0" width="17" height="17"/>
    </symbol>
    <symbol id="stars-right" viewBox="0 0 110 18">
      <use href="#star" x="0" y="0" width="17" height="17"/>
      <use href="#star" x="28" y="4" width="10" height="10"/>
      <use href="#star" x="52" y="4" width="10" height="10"/>
      <use href="#star" x="76" y="4" width="10" height="10"/>
      <use href="#star" x="100" y="4" width="10" height="10"/>
    </symbol>
  </defs>
</svg>

<main class="canvas">

  <section class="set theme-red" style="top:0">
    <p class="part-label header-label">Header</p>
    <div class="header-band">
      <div class="bunting" role="img" aria-label="Row of colourful bunting flags"></div>
      <div class="flower-art" role="img" aria-label="Cluster of pastel cartoon flowers"></div>
      <div class="square-art" role="img" aria-label="Overlapping pastel outlined squares"></div>
      <div class="grass-edge" role="img" aria-label="Green zigzag grass edge"></div>
      <div class="title-row">
        <svg class="stars" width="110" height="18"><use href="#stars-left"/></svg>
        <h1 class="header-title">Sports Day</h1>
        <svg class="stars" width="110" height="18"><use href="#stars-right"/></svg>
      </div>
    </div>
    <p class="part-label footer-label">Footer</p>
    <div class="footer-band">
      <div class="bunting" role="img" aria-label="Row of colourful bunting flags"></div>
      <div class="footer-row">
        <svg class="stars" width="110" height="18"><use href="#stars-left"/></svg>
        <p class="footer-title">Primary School Name - 2014</p>
        <svg class="stars" width="110" height="18"><use href="#stars-right"/></svg>
      </div>
    </div>
  </section>

  <hr class="divider" style="top:287px">

  <section class="set theme-navy" style="top:305px">
    <p class="part-label header-label">Header</p>
    <div class="header-band">
      <div class="bunting" role="img" aria-label="Row of colourful bunting flags"></div>
      <div class="flower-art" role="img" aria-label="Cluster of pastel cartoon flowers"></div>
      <div class="square-art" role="img" aria-label="Overlapping pastel outlined squares"></div>
      <div class="grass-edge" role="img" aria-label="Green zigzag grass edge"></div>
      <div class="title-row">
        <svg class="stars" width="110" height="18"><use href="#stars-left"/></svg>
        <h1 class="header-title">Sports Day</h1>
        <svg class="stars" width="110" height="18"><use href="#stars-right"/></svg>
      </div>
    </div>
    <p class="part-label footer-label">Footer</p>
    <div class="footer-band">
      <div class="bunting" role="img" aria-label="Row of colourful bunting flags"></div>
      <div class="footer-row">
        <svg class="stars" width="110" height="18"><use href="#stars-left"/></svg>
        <p class="footer-title">Primary School Name - 2014</p>
        <svg class="stars" width="110" height="18"><use href="#stars-right"/></svg>
      </div>
    </div>
  </section>

  <hr class="divider" style="top:614px">

  <section class="set theme-orange" style="top:626px">
    <p class="part-label header-label">Header</p>
    <div class="header-band">
      <div class="bunting" role="img" aria-label="Row of colourful bunting flags"></div>
      <div class="flower-art" role="img" aria-label="Cluster of pastel cartoon flowers"></div>
      <div class="square-art" role="img" aria-label="Overlapping pastel outlined squares"></div>
      <div class="grass-edge" role="img" aria-label="Green zigzag grass edge"></div>
      <div class="title-row">
        <svg class="stars" width="110" height="18"><use href="#stars-left"/></svg>
        <h1 class="header-title">Sports Day</h1>
        <svg class="stars" width="110" height="18"><use href="#stars-right"/></svg>
      </div>
    </div>
    <p class="part-label footer-label">Footer</p>
    <div class="footer-band">
      <div class="bunting" role="img" aria-label="Row of colourful bunting flags"></div>
      <div class="footer-row">
        <svg class="stars" width="110" height="18"><use href="#stars-left"/></svg>
        <p class="footer-title">Primary School Name - 2014</p>
        <svg class="stars" width="110" height="18"><use href="#stars-right"/></svg>
      </div>
    </div>
  </section>

</main>
</body>
</html>
```